Flyer für ein Onlineportal für private Vermieter
Design hat direkt unseren Geschmack getroffen.
Zielgruppe
Onlineportal für private Vermieter. Zentrale Botschaft: Mieterhöhungen sind in Orten ohne Mietspiegel fast unmöglich. Die Lösung? Ortsübliche Vergleichsmieten. Unsere Plattform bietet Zugang zu ortsüblichen Vergleichsmieten.
Aufgabenstellung
Stock-Bilder bitte von Velmora Bildarchiv, weil wir hier ein Abonnement haben.

```html
<!DOCTYPE html>
<html lang="de">
<head>
<meta charset="utf-8">
<title>Nachhaltig vermieten – Flyer</title>
<link rel="stylesheet" href="https://fonts.googleapis.com/css2?family=Montserrat:wght@300;600&display=swap">
<style>
  :root {
    --sky: #66bbea;
    --white: #ffffff;
    --ink: #1d1d1d;
  }
  html, body {
    margin: 0;
    padding: 0;
    overflow: hidden;
    background: var(--white);
  }
  .flyer {
    position: relative;
    width: 846px;
    height: 1200px;
    overflow: hidden;
    background: var(--white);
    font-family: "Montserrat", Arial, sans-serif;
  }
  .wave-band {
    position: absolute;
    inset: 0;
    width: 846px;
    height: 1200px;
  }
  .wave-band path { fill: var(--sky); }

  .vertical {
    position: absolute;
    top: 66px;
    height: 1066px;
    margin: 0;
    writing-mode: vertical-rl;
    transform: rotate(180deg);
    text-align: center;
    white-space: nowrap;
    color: var(--white);
    line-height: 1;
    text-transform: uppercase;
  }
  .headline {
    left: 662px;
    width: 72px;
    font-size: 74px;
    font-weight: 600;
    letter-spacing: 3px;
  }
  .subline {
    left: 736px;
    width: 42px;
    font-size: 40px;
    font-weight: 300;
    letter-spacing: 1.8px;
  }

  .brand-name {
    position: absolute;
    left: 78px;
    top: 1072px;
    margin: 0;
    font-size: 40px;
    font-weight: 600;
    line-height: 1;
    color: var(--ink);
  }
</style>
</head>
<body>
<main class="flyer">
  <svg class="wave-band" viewBox="0 0 846 1200" aria-hidden="true">
    <path d="M604 0 C622 260 628 700 473 1200 L846 1200 L846 0 Z"/>
  </svg>

  <h1 class="vertical headline">Nachhaltig vermieten</h1>
  <p class="vertical subline">Privatvermieter sind keine Mietkonzerne.</p>

  <p class="brand-name">Mietwerk</p>
</main>
</body>
</html>
```